Summer Special Membership Drive

Looking to run a "Summer Special" on 12 month Memberships for Jan/Feb 2020 to boost membership number up. This is a great time to get people exercising and everyone loves a New Year Sale. Special is designed to attract more people to join and enjoy the savings.
Artwork will be display via social media (FB and Instagram) as well as in store. Artwork must be eye catching and direct to the customer. Customer should feel a sense of relief with being able to exercise at a lower cost .

Artwork to be formatted in A0 for poster and Facebook cover and instagram

Heading: "Summer Sale or Summer Special"
12 Months
$350.00 Save over 20%
Terms and conditions apply"
*Offer End 28th February

New Opening Time
Weekdays from 5:00am starting 13th January

below are other promos we had designed on Artboard Hive along with potential photos to be included into this promo

Target Market(s)

16-50 male and female

Industry/Entity Type

Fitness

Colors

Designer to choose colors to be used in the design.

Requirements
Must have
• Lots of color and a summer theme. Attached is a 12 month special from last year.
• Contact details
• Address: 14 Marlow Rd Fenwick Park
• Ph: 9172 6581
• Web: www.brightlanefit.com.au
Nice to have
• Male and female in the artwork, They don't need to be the center of attention either

```html
<!DOCTYPE html>
<html lang="en">
<head>
<meta charset="utf-8">
<title>Brightlane Fitness – Summer Sale</title>
<link rel="stylesheet" href="https://fonts.googleapis.com/css2?family=Barlow:wght@400;500;600;700&family=Barlow+Condensed:wght@400;700&family=Gochi+Hand&display=swap">
<style>
  :root {
    --bg-top: #f8efc4;
    --bg-bottom: #f1cab9;
    --ink: #2b2927;
    --orange: #cf5a1a;
    --red-orange: #cc4416;
    --ribbon-red: #d63a17;
    --yellow: #f0cd2a;
    --yellow-soft: #eed35a;
    --band-line: #d4541c;
    --photo-light: #c7ab86;
    --photo-dark: #8c6d5c;
    --leaf: #bff0a4;
  }
  * { margin: 0; padding: 0; box-sizing: border-box; }
  html, body { width: 846px; height: 1200px; overflow: hidden; }
  body { font-family: "Barlow", Arial, sans-serif; color: var(--ink); }

  .poster {
    position: relative;
    width: 846px;
    height: 1200px;
    overflow: hidden;
    background: linear-gradient(180deg, var(--bg-top) 0%, #f5ddc0 55%, var(--bg-bottom) 100%);
  }

  .hero-photo {
    position: absolute;
    left: 420px; top: 30px;
    width: 426px; height: 1170px;
    border-radius: 200px 0 0 0;
    background: linear-gradient(90deg, rgba(199,171,134,0) 0%, var(--photo-light) 30%, var(--photo-dark) 100%);
    opacity: 0.85;
  }

  .leaf-decor {
    position: absolute;
    left: 30px; top: 155px;
    width: 210px; height: 300px;
    border-radius: 50%;
    background: radial-gradient(ellipse at center, rgba(191,240,164,0.75) 0%, rgba(191,240,164,0) 70%);
  }
  .leaf-decor--right {
    left: 520px; top: 360px;
    width: 150px; height: 130px;
  }

  .brand {
    position: absolute; left: 22px; top: 34px;
    font-weight: 700;
    font-size: 58px;
    line-height: 1;
    color: var(--ink);
    white-space: nowrap;
  }

  .headline-art { position: absolute; left: 0; top: 0; width: 846px; height: 660px; }

  .price-band, .offer-band, .hours-box {
    position: absolute;
    left: 0;
    background: linear-gradient(180deg, var(--yellow-soft), var(--yellow));
    border-bottom: 5px solid var(--band-line);
  }
  .price-band { top: 691px; width: 486px; height: 64px; }
  .offer-band { top: 767px; width: 486px; height: 64px; }
  .band-text {
    position: absolute; left: 16px; top: 6px;
    font-weight: 700; font-size: 43px; line-height: 52px;
    white-space: nowrap;
  }
  .price-old { position: relative; }
  .price-old::after {
    content: ""; position: absolute;
    left: 0; right: 10px; top: 52%;
    height: 3px; background: var(--ribbon-red);
  }
  .price-old sup { font-size: 20px; font-weight: 500; vertical-align: 4px; }
  .price-new {
    position: absolute; left: 326px; top: 652px;
    font-family: "Gochi Hand", cursive;
    font-size: 50px; line-height: 1;
    color: var(--ribbon-red);
  }

  .hours-box { top: 844px; width: 322px; height: 142px; padding: 12px 0 0 16px; border-bottom-width: 4px; }
  .hours-line { font-weight: 700; font-size: 28px; line-height: 36px; white-space: nowrap; }
  .hours-line--indent { padding-left: 10px; }
  .hours-line--light { font-weight: 400; }

  .contact-list { position: absolute; left: 24px; top: 1010px; list-style: none; }
  .contact-item {
    display: flex; align-items: center;
    height: 55px;
    font-size: 28px; letter-spacing: 0.5px;
    white-space: nowrap;
  }
  .contact-item svg { width: 32px; height: 38px; margin-right: 10px; flex: none; }

  .terms {
    position: absolute; right: 10px; bottom: 6px;
    font-size: 19px; letter-spacing: 0.5px;
  }
</style>
</head>
<body>
<main class="poster">
  <div class="hero-photo" role="img" aria-label="Photo of a woman in sportswear holding dumbbells, seen from behind"></div>
  <div class="leaf-decor" role="img" aria-label="Green palm leaf illustration"></div>
  <div class="leaf-decor leaf-decor--right" role="img" aria-label="Green palm leaf illustration"></div>

  <header class="brand">BRIGHTLANE FITNESS</header>

  <svg class="headline-art" viewBox="0 0 846 660" aria-label="Summer Sale, save over 20%">
    <g fill="none" stroke="var(--yellow)" stroke-width="3">
      <polygon class="frame" points="172,303 554,214 619,486 141,533"/>
      <polygon class="frame" points="157,266 575,246 601,473 128,465"/>
    </g>
    <text x="176" y="360" font-family="Barlow Condensed, sans-serif" font-weight="400" font-size="148" fill="var(--orange)" textLength="404" lengthAdjust="spacingAndGlyphs">SUMMER</text>
    <text x="176" y="523" font-family="Barlow Condensed, sans-serif" font-weight="700" font-size="205" fill="var(--red-orange)" textLength="404" lengthAdjust="spacingAndGlyphs">SALE</text>
    <g class="ribbon" fill="var(--yellow)">
      <polygon points="43,568 112,563 118,635 50,641 94,601"/>
      <polygon points="705,508 766,503 724,544 774,574 712,580"/>
      <polygon points="123,557 689,505 694,585 128,637"/>
    </g>
    <text transform="translate(134,622) rotate(-5.3)" font-family="Barlow, sans-serif" font-weight="700" font-size="70" fill="var(--ribbon-red)" textLength="552" lengthAdjust="spacingAndGlyphs">SAVE OVER 20%</text>
  </svg>

  <div class="price-new">$350.00</div>
  <section class="price-band">
    <div class="band-text">12 MONTHS for <span class="price-old">$450.00<sup>*</sup></span></div>
  </section>
  <section class="offer-band">
    <div class="band-text">OFFER ENDS FEB. 28th</div>
  </section>

  <section class="hours-box">
    <p class="hours-line">NEW OPENING TIME!</p>
    <p class="hours-line hours-line--indent">WEDNESDAYS 5AM</p>
    <p class="hours-line hours-line--light">STARTING JAN. 13TH</p>
  </section>

  <ul class="contact-list">
    <li class="contact-item">
      <svg viewBox="0 0 30 40"><path fill="var(--ink)" d="M15 1C7 1 1 7 1 15c0 10 14 24 14 24s14-14 14-24C29 7 23 1 15 1zm0 19a5.5 5.5 0 1 1 0-11 5.5 5.5 0 0 1 0 11z"/></svg>
      14 MARLOW RD FENWICK PARK
    </li>
    <li class="contact-item">
      <svg viewBox="0 0 30 40"><path fill="var(--ink)" d="M6 4l6-1 4 9-4 3c2 5 5 9 9 11l3-4 9 4-1 6c-1 2-3 3-6 3C13 33 3 20 3 9c0-2 1-4 3-5z"/></svg>
      9172 6581
    </li>
    <li class="contact-item">
      <svg viewBox="0 0 34 40"><g fill="none" stroke="var(--ink)" stroke-width="1.6"><circle cx="17" cy="20" r="15"/><ellipse cx="17" cy="20" rx="7" ry="15"/><line x1="2" y1="20" x2="32" y2="20"/><line x1="17" y1="5" x2="17" y2="35"/><path d="M5 12h24M5 28h24"/></g></svg>
      WWW.BRIGHTLANEFIT.COM.AU
    </li>
  </ul>

  <p class="terms">*TERMS AND CONDITIONS APPLY</p>
</main>
</body>
</html>
```